Business Card Design

We are a project managment company specializing in Interior fitout
PVH is for Commercial, Domestic, Industial - we provide managment to these industries and see the projects through design to contruction
Would like an area on the back of the card where peoplr can write notes
Thinking laser lines and architectural finishes
Colour theme at the moment is light grey and red although im open to any colour/design scheme

Industry/Entity Type

Business

Contact Information for Business Card

Norvale Ventures
Brett Lamonte
Managing Director
0487215694
brett@norvale-example.com.au

```html
<!DOCTYPE html>
<html lang="en">
<head>
<meta charset="utf-8">
<title>Norvale Ventures – Business Card</title>
<link rel="stylesheet" href="https://fonts.googleapis.com/css2?family=Playfair+Display:wght@500&family=Source+Sans+3:wght@400&display=swap">
<style>
  :root {
    --backdrop: #ececec;
    --card-blue: #3f5cb0;
    --card-blue-light: #5470c0;
    --card-grey: #b4b4b4;
    --card-black: #0b0b0b;
    --name-blue: #3656b4;
    --text-dark: #111111;
    --text-light: #ffffff;
  }
  * { box-sizing: border-box; margin: 0; padding: 0; }
  html, body {
    width: 1200px;
    height: 1200px;
    overflow: hidden;
    background: var(--backdrop);
  }
  .canvas {
    position: relative;
    width: 1200px;
    height: 1200px;
    display: flex;
    align-items: center;
    justify-content: center;
  }
  .card {
    position: relative;
    width: 1000px;
    height: 572px;
    background: var(--card-grey);
    overflow: hidden;
    box-shadow: 0 10px 30px rgba(0,0,0,0.18);
  }
  .card__header {
    position: absolute;
    left: 0; top: 0;
    width: 100%;
    height: 300px;
    background: radial-gradient(ellipse at 40% 45%, var(--card-blue-light), var(--card-blue) 70%);
  }
  .card__bands {
    position: absolute;
    left: 0; top: 0;
    width: 1000px;
    height: 572px;
  }
  .card__company {
    position: absolute;
    left: 0; right: 0;
    top: 140px;
    text-align: center;
    padding-left: 80px;
    font-family: "Playfair Display", serif;
    font-weight: 500;
    font-size: 60px;
    color: var(--text-light);
    letter-spacing: 0.5px;
    white-space: nowrap;
  }
  .card__person {
    position: absolute;
    left: 60px;
    top: 388px;
    font-family: "Source Sans 3", sans-serif;
  }
  .card__name {
    font-size: 44px;
    color: var(--name-blue);
    line-height: 1.1;
  }
  .card__title {
    font-size: 24px;
    color: var(--text-dark);
    text-transform: uppercase;
    letter-spacing: 0.3px;
    margin-top: 2px;
  }
  .card__contact {
    position: absolute;
    left: 560px;
    top: 440px;
    list-style: none;
    font-family: "Source Sans 3", sans-serif;
    font-size: 23px;
    color: var(--text-dark);
  }
  .card__contact li {
    display: flex;
    align-items: center;
    gap: 14px;
    height: 36px;
    white-space: nowrap;
  }
  .card__contact svg {
    width: 20px;
    height: 20px;
    flex: none;
  }
</style>
</head>
<body>
<main class="canvas">
  <section class="card">
    <div class="card__header" role="img" aria-label="Blue band with faint architectural floor-plan line drawing"></div>
    <svg class="card__bands" viewBox="0 0 1000 572" aria-hidden="true">
      <rect x="0" y="296" width="1000" height="18" fill="var(--card-black)"/>
      <polygon points="560,314 1000,314 1000,372 590,372" fill="var(--card-black)"/>
    </svg>
    <h1 class="card__company">Norvale Ventures</h1>
    <div class="card__person">
      <p class="card__name">Brett Lamonte</p>
      <p class="card__title">Managing Director</p>
    </div>
    <ul class="card__contact">
      <li>
        <svg viewBox="0 0 24 24" aria-hidden="true"><path fill="var(--text-dark)" d="M6.6 10.8a15.1 15.1 0 0 0 6.6 6.6l2.2-2.2a1 1 0 0 1 1-.25 11.4 11.4 0 0 0 3.6.57 1 1 0 0 1 1 1V20a1 1 0 0 1-1 1A17 17 0 0 1 3 4a1 1 0 0 1 1-1h3.5a1 1 0 0 1 1 1c0 1.25.2 2.45.57 3.57a1 1 0 0 1-.25 1z"/></svg>
        <span>0487215694</span>
      </li>
      <li>
        <svg viewBox="0 0 24 24" aria-hidden="true"><path fill="var(--text-dark)" d="M2 5h20v14H2z"/><path fill="none" stroke="var(--card-grey)" stroke-width="1.6" d="M2.5 5.5 12 13l9.5-7.5"/></svg>
        <span>brett@norvale-example.com.au</span>
      </li>
    </ul>
  </section>
</main>
</body>
</html>
```